Birch Lane Builders, Inc. Concrete cutting special flyer , 10% off for new customers

Flyer to send to potential customers and business associates and general contractors - specializing in Concrete-Flatwork
Concrete Repair
Concrete Sidewalks
Patios & Driveways
Stoops, Porches And Staircase
Foundation Contractors--Concrete
Facade Restoration
Concrete
Patios
Driveways
Walkways
Commercial Concrete Work
Concrete Restoration
Building Alterations
Foundations - Concrete
Concrete Repairs
blbofex.com

Target Market(s)

Homeowners, business owners & general contractors

Industry/Entity Type

Construction

Font styles to use
Serif

Colors
FFC000
F8CF3A
FAE287
FDF2CF
FEFAEE
EB3D1F
EC4F4E
F09395
F8D3D4
FCEDEE

Requirements
Must have
• General Contracting, masonry - Must have Logo Please see list of services Birch Lane Builders NY, Inc., has to offer. Concrete-Flatwork Concrete Repair Concrete Sidewalks Patios & Driveways Stoops, Porches And Staircase Foundation Contractors--Concrete Facade Restoration Concrete Patios Driveways Walkways Commercial Concrete Work Concrete Restoration Building Alterations Foundations - Concrete Concrete Repairs
Nice to have
• List of services - Logo - Black & Gold with a bold color to stand out (preferably reds)

```html
<!DOCTYPE html>
<html lang="en">
<head>
<meta charset="utf-8">
<title>Birch Lane Builders – Building on Trust</title>
<link rel="stylesheet" href="https://fonts.googleapis.com/css2?family=Noto+Serif:ital,wght@0,400;0,700;0,900;1,700;1,900&display=swap">
<style>
  :root{
    --red:#EB3D1F;
    --red-bright:#E8202A;
    --gold:#FFC000;
    --gold-soft:#F8CF3A;
    --ink:#141414;
    --charcoal:#262626;
    --white:#FFFFFF;
  }
  *{margin:0;padding:0;box-sizing:border-box}
  html,body{width:927px;height:1200px;overflow:hidden;background:var(--white)}
  .flyer{position:relative;width:927px;height:1200px;overflow:hidden;background:var(--white);font-family:"Noto Serif",Georgia,serif;color:var(--ink)}
  .shapes{position:absolute;inset:0;width:927px;height:1200px}
  .t{position:absolute;white-space:nowrap;line-height:1}

  .headline{font-weight:900;font-style:italic;color:var(--red-bright);font-size:84px;letter-spacing:-1px}
  .headline.one{top:34px;left:403px}
  .headline.two{top:112px;left:446px}

  .brand{left:62px;top:262px;display:flex;align-items:center;gap:10px;font-weight:700;font-size:19px;color:var(--ink)}
  .brand-mark{width:22px;height:22px;background:var(--gold)}

  .slogan{font-weight:900;font-style:italic;color:var(--white);font-size:60px;text-shadow:2px 3px 4px rgba(0,0,0,.55)}
  .slogan.one{left:42px;top:656px}
  .slogan.two{left:130px;top:718px}

  .intro{position:absolute;left:41px;top:784px;font-size:22.5px;line-height:30.3px;color:var(--white);white-space:nowrap}

  .services-title{left:678px;top:566px;font-weight:900;font-style:italic;font-size:25px;color:var(--ink)}
  .service{font-weight:700;font-size:20.5px;color:var(--ink)}
  .service::before{content:"";display:inline-block;width:8px;height:8px;border-radius:50%;background:var(--red-bright);margin-right:7px;vertical-align:4px}

  .offer{left:783px;top:897px;color:var(--red-bright);font-weight:900;text-align:left;line-height:.9}
  .offer .pct{display:block;font-size:44px}
  .offer .off{display:block;font-size:50px}
  .offer .who{display:block;font-size:16px;font-weight:700;line-height:1}
  .offer .who.small{font-size:14.5px}

  .web{right:40px;top:1028px;font-weight:900;font-size:46px;color:var(--ink);letter-spacing:-.5px}

  .call{left:88px;top:1091px;font-weight:900;font-size:38px;color:var(--gold)}
  .phones{left:356px;top:1092px;font-weight:700;font-size:39px;color:var(--white)}
  .phones .sep{color:var(--gold);margin:0 6px}

  .tagline{left:160px;top:1139px;font-weight:900;font-size:33px;color:var(--ink)}
  .tagline .sep{color:var(--red-bright);margin:0 14px}
</style>
</head>
<body>
<main class="flyer">
  <svg class="shapes" viewBox="0 0 1687 2184" preserveAspectRatio="none">
    <defs>
      <linearGradient id="skyFrame" x1="0" y1="0" x2="0.6" y2="1">
        <stop offset="0" stop-color="#8a8d92"/>
        <stop offset="0.45" stop-color="#c9b79a"/>
        <stop offset="1" stop-color="#6d6660"/>
      </linearGradient>
      <linearGradient id="workerTone" x1="0" y1="0" x2="1" y2="1">
        <stop offset="0" stop-color="#b58a78"/>
        <stop offset="0.5" stop-color="#d8b25a"/>
        <stop offset="1" stop-color="#7d6a52"/>
      </linearGradient>
      <linearGradient id="brickDark" x1="0" y1="0" x2="1" y2="1">
        <stop offset="0" stop-color="#3a3a3a"/>
        <stop offset="1" stop-color="#1f1f1f"/>
      </linearGradient>
    </defs>

    <polygon class="band-red" points="0,55 645,55 1215,1045 1085,1305 985,1305 1120,1060 595,145 0,145" fill="#E8202A"/>
    <polygon role="img" aria-label="Photo: timber wall framing with windows rising over a brick building under a cloudy sky" points="0,145 595,145 1120,1060 985,1305 0,1305" fill="url(#skyFrame)"/>
    <rect x="805" y="337" width="882" height="14" fill="#FFC000"/>
    <polygon role="img" aria-label="Photo: builder in plaid shirt holding a yellow hard hat, wearing a tool belt" points="812,351 1687,351 1687,1003 1185,1003" fill="url(#workerTone)"/>
    <polygon class="services-band" points="1215,1003 1687,1003 1687,1098 1200,1098 1230,1050" fill="#FFC000"/>
    <polygon role="img" aria-label="Photo: brick building wall under a dark overlay" points="0,1305 1085,1305 700,1980 0,1980" fill="url(#brickDark)"/>
    <polygon class="web-band" points="760,1855 1687,1855 1687,1978 695,1978" fill="#FFC000"/>
    <rect x="0" y="1978" width="1687" height="87" fill="#262626"/>
    <polygon class="phone-band" points="595,1978 1687,1978 1687,2065 640,2065" fill="#E8202A"/>
  </svg>

  <div class="t headline one">BUILDING</div>
  <div class="t headline two">ON TRUST</div>

  <div class="t brand"><span class="brand-mark"></span>Birch Lane Builders NY, Inc.</div>

  <div class="t slogan one">CONSTRUCTIVE</div>
  <div class="t slogan two">SOLUTIONS</div>

  <p class="intro">Our projects include both Residential<br>and Commercial construction,<br>repairs/restorations. Occupied and<br>fully operational job sites are<br>never a problem. And we can<br>also plan, manage, and build<br>multi-phase jobs. we specialize<br>in excavation, foundation,<br>Roofing and waterproofing.</p>

  <div class="t services-title">OUR SERVICES</div>
  <div class="t service" style="left:668px;top:620px">Concrete Repair</div>
  <div class="t service" style="left:645px;top:659px">Sidewalks</div>
  <div class="t service" style="left:621px;top:699px">Patios &amp; Driveways</div>
  <div class="t service" style="left:598px;top:738px">Stoops &amp; Porches</div>
  <div class="t service" style="left:575px;top:778px">Staircase</div>
  <div class="t service" style="left:552px;top:817px">Facade Restoration</div>
  <div class="t service" style="left:529px;top:856px">Commercial Concrete Work</div>
  <div class="t service" style="left:506px;top:896px">Concrete Restoration</div>
  <div class="t service" style="left:482px;top:935px">Building Alterations</div>
  <div class="t service" style="left:459px;top:975px">Foundations - Concrete</div>

  <div class="t offer">
    <span class="pct">10%</span>
    <span class="off">OFF</span>
    <span class="who">FOR NEW</span>
    <span class="who small">CUSTOMERS</span>
  </div>

  <div class="t web">www.blbofex.com</div>

  <div class="t call">Call or Text</div>
  <div class="t phones">555-201-4399<span class="sep">|</span>555-201-7901</div>

  <div class="t tagline">BUILD<span class="sep">|</span>RENOVATE<span class="sep">|</span>CONSTRUCT</div>
</main>
</body>
</html>
```